Interior designer needs a power point template design

I need a template PowerPoint design for my client presentations. The presentations I prepare for my clients usually include the furniture project, the detail of the selected furniture, and the costs. There are a lot of images I insert. What I need is to have a template that I can use for all my presentations, where from time to time I will insert the specific images and descriptions I want to insert. What will always be the same will be the cover, the colors, the font, and the design of the internal sections.
I already have my logo that I would like to insert on each page of the presentation (in small size).
In summary, I need:
- basic template design
- cover with an image chosen by Pixelmere photo
- design an internal section/chapter
- internal page design.

I like the clolors of pink and brown <8please see image attached)
Images (will come from Pixelmere photo)
● entrance/hall
● living room
● dining room
● Bathroom
● Closet
● Kids room
● Master bedroom
● Master bathroom
● Kitchen
● Office
● Laundry
● Balcony or Terrace

Target Market(s)

Customers (both residential and commercial projects)

Industry/Entity Type

interior design

Font styles to use
Other font styles liked:
• I like courier new

Requirements
Must have
• beautiful design
Should not have
• animations

```html
<!DOCTYPE html>
<html lang="it">
<head>
<meta charset="utf-8">
<title>Stanza Chiara – Template presentazione</title>
<link rel="stylesheet" href="https://fonts.googleapis.com/css2?family=Cormorant+Garamond:wght@500;600&display=swap">
<style>
  :root {
    --canvas: #f5bcab;
    --paper: #ffffff;
    --blush: #f4aa9a;
    --coral: #ee9488;
    --brick: #a82c24;
    --wine: #8a2a22;
    --cocoa: #4e2e26;
    --terracotta: #d4764e;
    --ink: #4a2a22;
    --logo: #8c7f7a;
  }
  * { box-sizing: border-box; margin: 0; padding: 0; }
  html, body { width: 872px; height: 1200px; overflow: hidden; }
  body {
    background: var(--canvas);
    font-family: "Cormorant Garamond", Georgia, serif;
    font-weight: 500;
    text-transform: uppercase;
    position: relative;
  }
  .slide {
    position: absolute;
    width: 352px; height: 198px;
    background: var(--paper);
    overflow: hidden;
    box-shadow: 1px 2px 3px rgba(90, 40, 30, .22);
  }
  .col-left { left: 52px; }
  .col-right { left: 465px; }
  .row-1 { top: 31px; } .row-2 { top: 263px; } .row-3 { top: 482px; }
  .row-4 { top: 705px; } .row-5 { top: 950px; }

  .abs { position: absolute; }
  .photo { position: absolute; }
  .title { font-size: 12.5px; line-height: 15px; letter-spacing: .2px; }
  .subtitle { font-size: 10.5px; line-height: 13px; letter-spacing: .2px; }

  .logo-mark {
    position: absolute; right: 14px; bottom: 12px;
    width: 18px; display: flex; flex-direction: column; align-items: center; gap: 2px;
  }
  .logo-mark .dot { width: 9px; height: 9px; border: .6px solid var(--logo); border-radius: 50%; }
  .logo-mark .name { font-size: 3.6px; line-height: 4px; color: var(--logo); text-align: center; letter-spacing: .2px; }
  .logo-mark.on-photo { background: var(--paper); padding: 3px 1px; right: 15px; bottom: 8px; }

  .brand-logo {
    position: absolute; display: flex; flex-direction: column; align-items: center; gap: 5px;
    color: var(--logo);
  }
  .brand-logo .dot { border: .8px solid var(--logo); border-radius: 50%; }
  .brand-logo .name { text-align: center; letter-spacing: 1px; }
</style>
</head>
<body>

<!-- Cover -->
<section class="slide col-left row-1">
  <div class="photo" style="left:4px;top:0;width:213px;height:198px;background:linear-gradient(160deg,#d9d9d6 0%,#6f6a62 35%,#4c5a3a 55%,#2f2a28 100%)" role="img" aria-label="Sala da pranzo elegante con lampadario, tavolo e vetrate sul giardino"></div>
  <div class="abs" style="left:221px;top:0;width:106px;height:113px;background:var(--blush)"></div>
  <h1 class="abs" style="left:226px;top:46px;color:#fff;font-weight:500;font-size:17.5px;line-height:21px">Camera<br>Padronale</h1>
  <div class="brand-logo" style="left:226px;top:139px;width:44px">
    <span class="dot" style="width:20px;height:20px"></span>
    <span class="name" style="font-size:6px;line-height:7px">Stanza<br>Chiara</span>
  </div>
  <div class="logo-mark"><span class="dot"></span><span class="name">Stanza<br>Chiara</span></div>
</section>

<!-- Section with three images -->
<section class="slide col-right row-1">
  <div class="abs" style="left:0;top:7px;width:352px;height:61px;background:var(--brick)"></div>
  <h2 class="abs title" style="left:18px;top:22px;color:#fff;font-weight:500">Camera Padronale</h2>
  <p class="abs subtitle" style="left:153px;top:22px;color:#f6d6cf">L’arredamento<br>della cabina<br>armadio</p>
  <div class="photo" style="left:18px;top:74px;width:104px;height:103px;background:linear-gradient(180deg,#e2b434,#d9a628)" role="img" aria-label="Sgabello in legno e metallo su fondo giallo"></div>
  <div class="photo" style="left:126px;top:74px;width:105px;height:103px;background:linear-gradient(180deg,#e6cdbf,#cdb4a0 70%,#9c9690)" role="img" aria-label="Comodino in legno con pianta"></div>
  <div class="photo" style="left:235px;top:74px;width:102px;height:103px;background:linear-gradient(160deg,#d46a5a,#b23a34 60%,#8c2a2a)" role="img" aria-label="Poltrona rossa in ambiente rosso con pianta"></div>
  <div class="logo-mark"><span class="dot"></span><span class="name">Stanza<br>Chiara</span></div>
</section>

<!-- Chapter: brown box -->
<section class="slide col-left row-2">
  <div class="photo" style="left:9px;top:0;width:170px;height:198px;background:linear-gradient(180deg,#ece8e4 0%,#d8d2cc 45%,#8a8480 70%,#3e3a38 100%)" role="img" aria-label="Divano bianco e tavolino in marmo con vasi rosa"></div>
  <div class="abs" style="left:167px;top:26px;width:179px;height:86px;background:var(--cocoa)"></div>
  <h2 class="abs title" style="left:187px;top:40px;color:var(--blush);font-weight:500">Camera Padronale</h2>
  <p class="abs subtitle" style="left:187px;top:62px;color:#fff">L’arredamento<br>della camera<br>padronale</p>
  <div class="logo-mark"><span class="dot"></span><span class="name">Stanza<br>Chiara</span></div>
</section>

<!-- Full-bleed image page -->
<section class="slide col-right row-2">
  <div class="photo" style="left:0;top:0;width:352px;height:198px;background:linear-gradient(170deg,#9a5a44 0%,#6a625e 35%,#b8875a 70%,#8a5e3c 100%)" role="img" aria-label="Soggiorno con divano grigio, poltrone e tavolino su parquet"></div>
  <h2 class="abs title" style="left:17px;top:8px;color:#fff;font-weight:500">Bagno Padronale</h2>
  <div class="logo-mark on-photo"><span class="dot"></span><span class="name">Stanza<br>Chiara</span></div>
</section>

<!-- Chapter: left text, right image -->
<section class="slide col-left row-3">
  <h2 class="abs title" style="left:18px;top:40px;color:var(--wine);font-weight:500">Camera<br>Padronale</h2>
  <p class="abs subtitle" style="left:18px;top:77px;color:var(--ink)">L’arredamento<br>della camera<br>padronale</p>
  <div class="photo" style="left:113px;top:0;width:239px;height:198px;background:linear-gradient(180deg,#e8e8e6 0%,#dcdcda 55%,#a8744c 70%,#c9c6c2 100%)" role="img" aria-label="Divano in pelle color cuoio contro parete chiara"></div>
  <div class="logo-mark on-photo"><span class="dot"></span><span class="name">Stanza<br>Chiara</span></div>
</section>

<!-- Internal page: band + image -->
<section class="slide col-right row-3">
  <div class="abs" style="left:0;top:0;width:352px;height:25px;background:var(--brick)"></div>
  <h2 class="abs title" style="left:18px;top:6px;color:#fff;font-weight:500">Bagno Padronale</h2>
  <p class="abs subtitle" style="left:18px;top:28px;color:var(--ink)">L’arredamento<br>del bagno padronale</p>
  <div class="photo" style="left:18px;top:56px;width:282px;height:137px;background:linear-gradient(180deg,#dcdcdc 0%,#d2b48e 40%,#c9a478 75%,#8d8e90 100%)" role="img" aria-label="Cassettiera in legno chiaro con libri e pianta"></div>
  <div class="logo-mark"><span class="dot"></span><span class="name">Stanza<br>Chiara</span></div>
</section>

<!-- Internal page: pink band + two images -->
<section class="slide col-left row-4">
  <div class="abs" style="left:18px;top:0;width:179px;height:49px;background:var(--coral)"></div>
  <h2 class="abs title" style="left:34px;top:9px;color:#fff;font-weight:500">Cabina Armadio</h2>
  <div class="photo" style="left:18px;top:57px;width:179px;height:131px;background:linear-gradient(180deg,#e9e6e2 0%,#dcd6d0 55%,#d4692a 70%,#8a8784 100%)" role="img" aria-label="Divano in pelle arancione con luce naturale"></div>
  <div class="photo" style="left:201px;top:57px;width:112px;height:130px;background:linear-gradient(180deg,#ecebe8 0%,#e0dcd6 55%,#b08c62 100%)" role="img" aria-label="Scrivania e sedia in legno vicino alla finestra"></div>
  <div class="logo-mark"><span class="dot"></span><span class="name">Stanza<br>Chiara</span></div>
</section>

<!-- Internal page: image left, text right -->
<section class="slide col-right row-4">
  <div class="photo" style="left:0;top:0;width:185px;height:198px;background:linear-gradient(180deg,#c89882 0%,#b88a6c 45%,#cdb69a 70%,#6e6560 100%)" role="img" aria-label="Divano grigio con cuscini e piante su colonne in legno"></div>
  <h2 class="abs title" style="left:198px;top:8px;color:var(--wine);font-weight:500">Bagno Padronale</h2>
  <p class="abs subtitle" style="left:198px;top:27px;color:var(--ink)">L’arredamento<br>del bagno padronale</p>
  <div class="abs" style="left:198px;top:63px;width:154px;height:3px;background:var(--blush)"></div>
  <div class="logo-mark"><span class="dot"></span><span class="name">Stanza<br>Chiara</span></div>
</section>

<!-- Chapter: pink column -->
<section class="slide col-left row-5">
  <div class="abs" style="left:36px;top:0;width:103px;height:198px;background:var(--blush)"></div>
  <h2 class="abs title" style="left:42px;top:8px;color:#fff;font-weight:500">Cabina<br>Armadio</h2>
  <p class="abs subtitle" style="left:42px;top:44px;color:var(--ink)">L’arredamento<br>della cabina<br>armadio</p>
  <div class="photo" style="left:139px;top:5px;width:203px;height:188px;background:linear-gradient(100deg,#2e302c 0%,#2e302c 15%,#e6e4e0 16%,#dcd8d2 60%,#a47a52 100%)" role="img" aria-label="Poltrona gialla con lampada da terra e quadro"></div>
  <div class="logo-mark on-photo" style="right:14px;bottom:9px"><span class="dot"></span><span class="name">Stanza<br>Chiara</span></div>
</section>

<!-- Closing: contacts -->
<section class="slide col-right row-5">
  <div class="photo" style="left:4px;top:0;width:172px;height:198px;background:linear-gradient(180deg,#e6ddd2 0%,#d8c8b4 45%,#8a6a48 55%,#e2ddd6 80%,#cfc8c0 100%)" role="img" aria-label="Tavolo rotondo in legno con sedie bianche e pianta"></div>
  <div class="abs" style="left:178px;top:0;width:174px;height:85px;background:var(--terracotta)"></div>
  <h2 class="abs" style="left:183px;top:7px;color:#fff;font-weight:500;font-size:17.5px;line-height:20px">Stanza Chiara</h2>
  <address class="abs" style="left:183px;top:30px;color:#fff;font-style:normal;font-size:8.6px;line-height:12.4px">
    di Marta Verani<br>Via delle Rose, 42<br>marta.verani@mailbox.it<br>345/6182093
  </address>
  <div class="brand-logo" style="left:186px;top:100px;width:60px">
    <span class="dot" style="width:36px;height:36px"></span>
    <span class="name" style="font-size:9px;line-height:10px">Stanza<br>Chiara</span>
  </div>
  <div class="logo-mark"><span class="dot"></span><span class="name">Stanza<br>Chiara</span></div>
</section>

</body>
</html>
```